Lantern Square, Steady Course. (Website Design)

We are launching a new bipartisan civic movement: Lantern Square. Steady Course.
The mission is this: Americans deserve a government that is legally required to serve them honestly.
We are looking for a world-class website designer capable of creating an emotionally powerful, modern, cinematic landing page experience that feels larger than politics.
This is not a campaign website for a political party or candidate. We are not looking for a red, white, and blue page with stripes, or American flags, or stock footage of smiling people in a voting booth. We are looking for an emotional and cinematic experience through and through.
The visual direction should feel:
Historic
Hopeful
American
Emotional
Cinematic
Trustworthy
Timeless
The goal is to make visitors feel that they are witnessing the beginning of something important and want to be part of it in the end.
Primary Objective:
Inspire visitors to participate in a one-minute survey and cast their vote.
The survey itself is extremely short and takes approximately one minute to complete.
Everything on the page should ultimately guide visitors toward this action while creating enough curiosity, trust, emotional engagement, and excitement that they feel compelled to take part in the movement.
Audience:
The audience is ordinary Americans across the political spectrum: Democrats, Republicans, Independents.
The design should feel unifying and welcoming.
It should avoid looking partisan, ideological, activist, or government-issued.
Creative Freedom:
We are intentionally giving designers substantial creative freedom.
We are not looking for someone to simply arrange content into predefined sections.
Instead, we are looking for a designer who can think strategically about user experience and persuasion.
The ideal design is as minimal as possible, but you may always:
Use as many sections as you believe are necessary.
Use as many images as you believe are necessary.
Include storytelling elements.
Include data visualizations.
Include timelines.
Include videos.
Include animations.
Include or exclude sections as you see fit.
Reorganize the flow entirely.
We uploaded some files containing text and section suggestions. You don’t have to use them.
We also uploaded some images to convey the general feel we’re looking for.
We are much more interested in the effectiveness of the overall experience than in any specific layout.
What success looks like:
Think outside the box.
Please do not create another generic political website. We have already explored those approaches.
We are looking for something different.
The winning design will be the one that most effectively guides visitors from curiosity to belief to participation.
When a visitor reaches the end of the experience, they should feel:
This is bigger than politics.
This is something I can support regardless of party.
This feels credible.
This feels hopeful.
I want to be part of this.
Use the survey results, the research findings, the principles, the storytelling, or any other elements you believe will help build trust and inspire participation.
Don't just impress us with flashy visuals. Impress us with a website experience that inspires people to become part of the movement and cast their vote.
The final call-to-action should feel like the natural conclusion of the journey, not a request for engagement.
Our goal is not simply to inform visitors. Our goal is to inspire them to cast their vote.
Prioritize emotional impact, storytelling, clarity, and persuasion over decorative design elements.
Final words:
Design a website experience that successfully inspires visitors to take the survey and cast their vote.
Think like a storyteller, not just a designer.
Thank you for your interest in the project.
Best of luck.

```html
<!DOCTYPE html>
<html lang="en">
<head>
<meta charset="utf-8">
<title>Lantern Square, Steady Course.</title>
<link href="https://fonts.googleapis.com/css2?family=Poppins:ital,wght@0,400;0,500;0,600;0,700;1,500;1,600&family=Playfair+Display:ital,wght@1,400;1,500&display=swap" rel="stylesheet">
<style>
:root{
  --red:#b21e2b;
  --red-deep:#8f1622;
  --navy:#0f2258;
  --navy-deep:#0a1a46;
  --ink:#1a2444;
  --muted:#4a5170;
  --lav:#eceef6;
  --white:#ffffff;
  --sans:'Poppins', sans-serif;
  --serif:'Playfair Display', serif;
}
*{box-sizing:border-box;margin:0;padding:0}
html,body{width:1200px;height:5119px;overflow:hidden}
body{position:relative;font-family:var(--sans);color:var(--ink);background:var(--white)}
.abs{position:absolute}
.serif{font-family:var(--serif);font-style:italic;font-weight:400}
.eyebrow{font-size:11px;font-weight:600;color:var(--red);letter-spacing:.3px;text-transform:uppercase}

/* top bar */
.topbar{left:0;top:0;width:1200px;height:34px;background:var(--red)}
.topbar .socials{left:141px;top:11px;display:flex;gap:12px}
.topbar .socials span{width:11px;height:11px;border-radius:50%;background:var(--white);display:block}
.topbar .mail{right:135px;top:9px;color:var(--white);font-size:12px;display:flex;align-items:center;gap:6px}

/* header */
.header{left:0;top:34px;width:1200px;height:84px;background:var(--white)}
.brand{display:flex;align-items:center;gap:10px}
.brand .mark{width:62px;height:62px;border-radius:50%;background:var(--navy)}
.brand .name{font-weight:600;font-size:15px;line-height:1.1;color:var(--navy);width:110px}
.header .brand{left:141px;top:11px}
.nav{left:507px;top:32px;display:flex;gap:26px;font-size:12px;font-weight:500;color:var(--ink)}
.btn-vote{left:932px;top:20px;width:132px;height:44px;border-radius:22px;background:var(--navy);color:var(--white);font-size:12px;font-weight:600;display:flex;align-items:center;justify-content:center;gap:8px}

/* hero */
.hero{left:0;top:118px;width:1200px;height:564px;background:linear-gradient(180deg,#2a3f78 0%,#22366d 40%,#1b2d5e 75%,#27385f 100%)}
.hero-copy{left:0;top:168px;width:1200px;text-align:center;color:var(--white)}
.hero-copy .kicker{font-size:11px;font-weight:600;letter-spacing:.3px}
.hero-copy h1{font-size:48px;font-weight:600;line-height:1.02;margin-top:6px}
.hero-copy h1 .serif{font-size:50px}
.hero-copy p{font-size:13px;line-height:1.4;margin-top:16px}
.play{left:562px;top:367px;width:76px;height:76px;border-radius:50%;background:var(--white);display:flex;align-items:center;justify-content:center;box-shadow:0 0 0 8px rgba(255,255,255,.18)}

/* stats */
.stats{left:0;top:682px;width:1200px;height:119px;background:linear-gradient(90deg,var(--red) 0%,#7a1d3e 45%,var(--navy) 100%)}
.stat{top:32px;display:flex;align-items:center;gap:12px;color:var(--white)}
.stat .num{font-size:34px;font-weight:700;line-height:1}
.stat .lbl{font-size:11px;margin-top:4px}

/* mission */
.ph{border-radius:0}
.mission-title{left:576px;top:912px;font-size:40px;font-weight:600;color:var(--navy)}
.underline{left:578px;top:962px}
.mission-lead{left:576px;top:978px;width:480px;font-size:15px;font-style:italic;font-weight:500;color:var(--navy);line-height:1.55}
.mission-body{left:576px;top:1036px;width:490px;font-size:12px;line-height:2.1;color:var(--ink)}

/* who */
.who-band{left:0;top:1621px;width:1200px;height:583px;background:var(--navy)}
.who-title{left:141px;top:1712px;font-size:40px;font-weight:600;color:var(--white)}
.who-body{left:141px;top:1778px;width:410px;font-size:12px;line-height:1.6;color:var(--white)}
.who-body p{margin-bottom:14px}
.who-photos{left:141px;top:1933px;display:flex;gap:6px}
.who-photos div{width:132px;height:151px}

/* journey */
.center-head{left:0;width:1200px;text-align:center}
.center-head h2{font-size:40px;font-weight:600;color:var(--navy);line-height:1.2}
.center-head h2 .serif{font-size:42px}
.tl-line{left:0;top:2582px;width:1200px;height:6px;background:linear-gradient(90deg,rgba(178,30,43,0) 0%,var(--red) 15%,var(--red) 30%,var(--navy) 30%,var(--navy) 50%,var(--red) 50%,var(--red) 70%,var(--navy) 70%,var(--navy) 85%,rgba(15,34,88,0) 100%)}
.node{width:26px;height:26px;border-radius:50%;color:var(--white);font-size:10px;font-weight:600;display:flex;align-items:center;justify-content:center;border:3px solid var(--white)}
.yr{width:78px;height:78px;border-radius:50%;color:var(--white);font-size:21px;font-weight:600;display:flex;align-items:center;justify-content:center;border:4px solid var(--white);box-shadow:0 3px 10px rgba(0,0,0,.15)}
.stem{width:3px}
.tbox{width:196px;height:128px;background:var(--white);border:2px solid var(--navy);box-shadow:4px 4px 0 rgba(15,34,88,.15);text-align:center;padding:14px 14px 0}
.tbox.red{border-color:var(--red)}
.tbox h4{font-size:15px;font-weight:600;color:var(--navy);margin-bottom:4px}
.tbox p{font-size:11px;line-height:1.45;color:var(--ink)}
.journey-close{left:0;top:2806px;width:1200px;text-align:center;font-size:15px;font-weight:600;color:var(--ink)}

/* principles */
.principles{left:0;top:2901px;width:1200px;height:775px;background:var(--lav)}
.orbit{left:418px;top:3114px}
.core{left:455px;top:3151px;width:286px;height:286px;border-radius:50%;background:radial-gradient(circle at 50% 40%,#6a6a72 0%,#3c3c46 55%,#24242d 100%)}
.core-text{left:455px;top:3255px;width:286px;text-align:center;color:var(--white)}
.core-text .big{font-size:36px;font-weight:700;line-height:1}
.core-text .small{font-size:21px;font-weight:600;margin-top:6px}
.pico{width:64px;height:64px;border-radius:50%;background:var(--white);box-shadow:0 4px 12px rgba(15,34,88,.15);display:flex;align-items:center;justify-content:center}
.pnum{width:24px;height:24px;border-radius:50%;background:var(--red);color:var(--white);font-size:9px;font-weight:600;display:flex;align-items:center;justify-content:center;border:2px solid var(--white)}
.ptext h4{font-size:14px;font-weight:600;color:var(--navy);margin-bottom:3px}
.ptext p{font-size:11px;line-height:1.6;color:var(--ink)}
.ptext.right{text-align:right}
.ptext.mid{text-align:center}

/* survey */
.card{left:141px;top:3861px;width:924px;height:480px;background:var(--white);box-shadow:0 4px 24px rgba(15,34,88,.14)}
.row{left:24px;width:876px;display:flex;justify-content:space-between;align-items:center;border-bottom:1px solid #e3e5ee;height:64px}
.row .k{font-size:15px;font-weight:600;color:var(--navy)}
.row .v{font-size:32px;font-weight:700;color:var(--red)}
.row.last{border-bottom:none}
.stress{left:20px;top:335px;width:884px;height:120px;background:var(--lav);text-align:center;font-size:11px;color:var(--ink);padding-top:22px;line-height:2.55}
.stress b{font-weight:600;color:var(--navy)}

/* cta */
.cta{left:141px;top:4425px;width:924px;height:364px;background:linear-gradient(100deg,var(--red) 0%,#a61d2a 45%,#c0343b 70%,var(--red-deep) 100%)}
.cta h2{left:45px;top:42px;font-size:40px;font-weight:600;color:var(--white);line-height:1.22}
.cta h2 .serif{font-size:42px}
.cta p{left:45px;top:212px;width:560px;font-size:12px;line-height:1.6;color:var(--white)}
.cta .btn{left:45px;top:284px;width:134px;height:44px;border-radius:22px;background:var(--white);color:var(--navy);font-size:12px;font-weight:600;display:flex;align-items:center;justify-content:center;gap:8px}
.count{left:666px;top:80px;width:186px;height:238px;background:var(--white);text-align:center;padding-top:18px}
.count .n{font-size:58px;font-weight:600;color:var(--navy);line-height:1;margin-top:14px}
.count .l{font-size:12px;color:var(--ink);line-height:1.4;margin-top:8px}

/* footer */
.footer{left:0;top:4868px;width:1200px;height:251px;background:var(--navy)}
.footer .brand{left:477px;top:40px}
.footer .brand .mark{background:var(--white)}
.footer .brand .name{color:var(--white)}
.fsocial{left:502px;top:130px;display:flex;gap:10px}
.fsocial span{width:30px;height:30px;border-radius:50%;border:2px solid var(--white);display:block}
.fsocial span.on{background:var(--red);border-color:var(--red)}
.frule{left:0;top:189px;width:1200px;height:1px;background:rgba(255,255,255,.2)}
.copy{left:0;top:210px;width:1200px;text-align:center;font-size:12px;color:var(--white)}
</style>
</head>
<body>

<!-- top bar -->
<div class="abs topbar">
  <div class="abs socials"><span></span><span></span><span></span><span></span></div>
  <div class="abs mail">
    <svg width="13" height="10" viewBox="0 0 13 10"><rect x=".5" y=".5" width="12" height="9" fill="none" stroke="#fff"/><path d="M.5 .5l6 5 6-5" fill="none" stroke="#fff"/></svg>
    Email: hello@lanternsquare.org
  </div>
</div>

<!-- header -->
<header class="abs header">
  <div class="abs brand"><span class="mark"></span><span class="name">Lantern Square</span></div>
  <nav class="abs nav"><span>MISSION</span><span>JOURNEY</span><span>PRINCIPLES</span><span>EVIDENCE</span><span>ACT NOW</span></nav>
  <div class="abs btn-vote">VOTE YES
    <svg width="22" height="10" viewBox="0 0 22 10"><path d="M0 5h20M16 1l4 4-4 4" fill="none" stroke="#fff" stroke-width="1.6"/></svg>
  </div>
</header>

<!-- hero -->
<section class="abs hero" role="img" aria-label="Photograph of the Capitol dome under a cloudy blue sky, framed by trees"></section>
<div class="abs hero-copy">
  <div class="kicker">A MOVEMENT FOR PUBLIC SERVICE</div>
  <h1>Our Government Should<br>Be Legally <span class="serif">Required To Serve Us.</span></h1>
  <p>A Bipartisan Movement To Make Honesty, Transparency, And The Public<br>Interest The Legal Standard Of Government.</p>
</div>
<div class="abs play"><svg width="22" height="24" viewBox="0 0 22 24"><path d="M3 2l17 10L3 22z" fill="var(--red)"/></svg></div>

<!-- stats -->
<section class="abs stats">
  <div class="abs stat" style="left:141px">
    <svg width="48" height="46" viewBox="0 0 48 46" fill="none" stroke="#fff" stroke-width="2.5"><rect x="14" y="2" width="22" height="40" rx="3"/><rect x="4" y="16" width="18" height="16"/><path d="M9 24l3 3 6-6"/></svg>
    <div><div class="num">82.9%</div><div class="lbl">SAID YES IN A BALLOT VOTE.</div></div>
  </div>
  <div class="abs stat" style="left:427px">
    <svg width="52" height="46" viewBox="0 0 52 46" fill="none" stroke="#fff" stroke-width="2.5"><rect x="18" y="2" width="16" height="18"/><path d="M4 20l10 10h24l10-10M14 30v14M38 30v14"/></svg>
    <div><div class="num">89.9%</div><div class="lbl">SAID THEY AGREE WITH &nbsp;THE 7 PRINCIPLES.</div></div>
  </div>
  <div class="abs stat" style="left:795px">
    <svg width="64" height="46" viewBox="0 0 64 46" fill="none" stroke="#fff" stroke-width="2.5"><rect x="22" y="2" width="20" height="16"/><circle cx="12" cy="22" r="5"/><circle cx="32" cy="26" r="5"/><circle cx="52" cy="22" r="5"/><path d="M2 44c0-8 4-12 10-12s10 4 10 12M22 44c0-6 4-10 10-10s10 4 10 10M42 44c0-8 4-12 10-12s10 4 10 12"/></svg>
    <div><div class="num">1,016</div><div class="lbl">PEOPLE ALREADY VOTED FOR IT.</div></div>
  </div>
</section>

<!-- mission -->
<div class="abs ph" style="left:141px;top:876px;width:384px;height:326px;background:linear-gradient(160deg,#cfc9bd,#8c877d 60%,#5a574f)" role="img" aria-label="Black and white archival photograph of a demonstrator in front of the Capitol"></div>
<div class="abs ph" style="left:141px;top:1202px;width:384px;height:262px;background:linear-gradient(160deg,#e6e6e4,#9a9894 55%,#3c3b38)" role="img" aria-label="Black and white archival photograph of a civil rights speaker raising his hand"></div>
<div class="abs eyebrow" style="left:576px;top:896px">CORE PURPOSE</div>
<h2 class="abs mission-title">Mission <span class="serif">Statement</span></h2>
<svg class="abs underline" width="150" height="10" viewBox="0 0 150 10"><path d="M2 7Q75 1 148 6" fill="none" stroke="var(--red)" stroke-width="3" stroke-linecap="round"/></svg>
<p class="abs mission-lead">Today, Not A Single Law Binds Our Government To Act Honestly, Fully, And In Our Best Interest</p>
<div class="abs mission-body">If Our Government Exists Solely To Serve Us, Why Isn’t It Legally Required To?<br>We Founded This Movement To Change That.</div>
<div class="abs ph" style="left:576px;top:1117px;width:483px;height:338px;background:linear-gradient(135deg,#e9d3b8 0%,#e2a15a 35%,#b5512f 65%,#4a3a52 100%)" role="img" aria-label="Sunlit photograph of a statue and a flag held aloft against a warm sky"></div>

<!-- who we are -->
<section class="abs who-band"></section>
<div class="abs ph" style="left:640px;top:1520px;width:560px;height:684px;background:linear-gradient(180deg,rgba(220,224,234,0) 0%,#cfd4e1 18%,#aeb6ca 55%,#a45364 85%,#8a2a3d 100%)" role="img" aria-label="Photograph of the Capitol dome and facade fading into red"></div>
<div class="abs eyebrow" style="left:141px;top:1696px;color:var(--white)">ABOUT US</div>
<h2 class="abs who-title">Who <span class="serif">We Are</span></h2>
<div class="abs who-body">
  <p>We Are A Bipartisan Movement Based In Washington, D.C.</p>
  <p>We Believe Americans Deserve A Government Legally Required To Act Honestly, Transparently, And In The Public’s Best Interest.</p>
  <p>At A Time Of Growing Division And Distrust, We Are Working To Unite Americans Around A Simple Idea: Government Should Faithfully Serve The People, Not Special Interests.</p>
</div>
<div class="abs who-photos">
  <div style="background:linear-gradient(160deg,#b9b4aa,#4b4842)" role="img" aria-label="Archival portrait of a civil rights activist"></div>
  <div style="background:linear-gradient(160deg,#d8a850,#6a4a1c)" role="img" aria-label="Archival portrait of a civil rights leader"></div>
  <div style="background:linear-gradient(160deg,#dcdad6,#55534f)" role="img" aria-label="Archival portrait of a civil rights activist"></div>
</div>

<!-- journey -->
<div class="abs center-head" style="top:2298px">
  <div class="eyebrow">OUR JOURNEY</div>
  <h2>Our Journey <span class="serif">To A National Movement.</span></h2>
</div>
<svg class="abs" style="left:520px;top:2364px" width="180" height="10" viewBox="0 0 180 10"><path d="M2 7Q90 1 178 6" fill="none" stroke="var(--red)" stroke-width="3" stroke-linecap="round"/></svg>
<div class="abs tl-line"></div>

<!-- 01 -->
<div class="abs yr" style="left:201px;top:2439px;background:var(--red)">2024</div>
<div class="abs stem" style="left:239px;top:2517px;height:55px;background:var(--red)"></div>
<div class="abs node" style="left:227px;top:2572px;background:var(--red)">01</div>
<div class="abs stem" style="left:239px;top:2598px;height:30px;background:var(--red)"></div>
<div class="abs tbox red" style="left:143px;top:2627px"><h4>August 2024</h4><p>We Started A Nonprofit With This Goal In Mind:Americans Deserve An Honest Government.</p></div>
<!-- 02 -->
<div class="abs tbox" style="left:378px;top:2414px"><h4>October 2025</h4><p>We Identified 10 Principles That Most Of Americans Agree Our Government Must Uphold.</p></div>
<div class="abs stem" style="left:476px;top:2542px;height:30px;background:var(--navy)"></div>
<div class="abs node" style="left:464px;top:2572px;background:var(--navy)">02</div>
<div class="abs stem" style="left:476px;top:2598px;height:51px;background:var(--navy)"></div>
<div class="abs yr" style="left:438px;top:2649px;background:var(--navy)">2025</div>
<!-- 03 -->
<div class="abs yr" style="left:672px;top:2439px;background:var(--red)">2026</div>
<div class="abs stem" style="left:710px;top:2517px;height:55px;background:var(--red)"></div>
<div class="abs node" style="left:698px;top:2572px;background:var(--red)">03</div>
<div class="abs stem" style="left:710px;top:2598px;height:30px;background:var(--red)"></div>
<div class="abs tbox red" style="left:614px;top:2627px"><h4>March 2026</h4><p>We Turned Those Principles Into A Rigorous Framework And Named It Lantern Square, Steady Course.</p></div>
<!-- 04 -->
<div class="abs tbox" style="left:856px;top:2414px"><h4>April 2026</h4><p>We Tested The Framework In A Pre-Registered National Study With Americans Across The Political Spectrum.</p></div>
<div class="abs stem" style="left:953px;top:2542px;height:30px;background:var(--navy)"></div>
<div class="abs node" style="left:941px;top:2572px;background:var(--navy)">04</div>
<div class="abs stem" style="left:953px;top:2598px;height:51px;background:var(--navy)"></div>
<div class="abs yr" style="left:915px;top:2649px;background:var(--navy)">2026</div>
<div class="abs journey-close">And The Results Exceeded All Our Expectation.</div>

<!-- principles -->
<section class="abs principles"></section>
<div class="abs center-head" style="top:2983px">
  <div class="eyebrow">THE SEVEN PRINCIPLES</div>
  <h2>The Seven <span class="serif">7Principles</span></h2>
</div>
<svg class="abs" style="left:470px;top:3050px" width="130" height="10" viewBox="0 0 130 10"><path d="M2 7Q65 1 128 6" fill="none" stroke="var(--red)" stroke-width="3" stroke-linecap="round"/></svg>
<svg class="abs orbit" width="360" height="360" viewBox="0 0 360 360"><circle cx="180" cy="180" r="176" fill="none" stroke="#b9bfd6" stroke-width="1.5" stroke-dasharray="4 5"/></svg>
<div class="abs core" role="img" aria-label="Sepia portrait of a historic statesman in front of a flag"></div>
<div class="abs core-text"><div class="big">89.9%*</div><div class="small">Said Agree</div></div>

<!-- chevrons -->
<svg class="abs" style="left:412px;top:3206px" width="16" height="16" viewBox="0 0 16 16"><path d="M3 3l5 5 5-5M3 9l5 5 5-5" fill="none" stroke="var(--red)" stroke-width="2"/></svg>
<svg class="abs" style="left:416px;top:3342px" width="16" height="16" viewBox="0 0 16 16"><path d="M3 3l5 5 5-5M3 9l5 5 5-5" fill="none" stroke="var(--red)" stroke-width="2"/></svg>
<svg class="abs" style="left:658px;top:3454px" width="16" height="16" viewBox="0 0 16 16"><path d="M3 3l5 5-5 5M9 3l5 5-5 5" fill="none" stroke="var(--red)" stroke-width="2"/></svg>
<svg class="abs" style="left:766px;top:3206px" width="16" height="16" viewBox="0 0 16 16"><path d="M3 13l5-5 5 5M3 7l5-5 5 5" fill="none" stroke="var(--red)" stroke-width="2"/></svg>

<!-- icons -->
<div class="abs pico" style="left:413px;top:3103px"><svg width="30" height="30" viewBox="0 0 30 30" fill="var(--navy)"><circle cx="15" cy="7" r="4"/><circle cx="8" cy="14" r="3"/><circle cx="22" cy="14" r="3"/><path d="M9 28c0-7 3-10 6-10s6 3 6 10z"/><path d="M3 26c0-5 2-7 5-7s4 2 4 4M27 26c0-5-2-7-5-7s-4 2-4 4"/></svg></div>
<div class="abs pico" style="left:359px;top:3254px"><svg width="30" height="30" viewBox="0 0 30 30" fill="none" stroke="var(--navy)" stroke-width="2.5"><path d="M6 18V9M11 16V5M16 16V4M21 16V7M6 18c0 6 4 9 9 9 6 0 9-4 10-10l1-5"/><circle cx="20" cy="22" r="4" fill="var(--white)"/><path d="M18 22l1.5 1.5L22 21"/></svg></div>
<div class="abs pico" style="left:421px;top:3386px"><svg width="30" height="30" viewBox="0 0 30 30" fill="var(--navy)"><rect x="14" y="3" width="2" height="24"/><rect x="6" y="6" width="18" height="2"/><path d="M3 17l4-9 4 9z"/><path d="M19 17l4-9 4 9z"/><rect x="9" y="25" width="12" height="3"/></svg></div>
<div class="abs pico" style="left:566px;top:3435px"><svg width="30" height="30" viewBox="0 0 30 30" fill="var(--navy)"><circle cx="16" cy="5" r="3"/><path d="M13 9h6l-2 8 4 6h-3l-4-5-3 5H8l4-7z"/><path d="M2 28l8-6 6 3 12-10v13z"/></svg></div>
<div class="abs pico" style="left:707px;top:3390px"><svg width="30" height="30" viewBox="0 0 30 30" fill="var(--navy)"><rect x="4" y="8" width="12" height="14" rx="1"/><rect x="16" y="11" width="8" height="8"/><path d="M24 9l4-3M24 15h4M24 21l4 3" stroke="var(--navy)" stroke-width="2"/><rect x="7" y="22" width="4" height="6"/></svg></div>
<div class="abs pico" style="left:773px;top:3254px"><svg width="30" height="30" viewBox="0 0 30 30" fill="var(--navy)"><path d="M15 2l2 3h-4z"/><path d="M8 12a7 6 0 0 1 14 0z"/><rect x="5" y="12" width="20" height="2"/><rect x="7" y="15" width="2" height="9"/><rect x="12" y="15" width="2" height="9"/><rect x="16" y="15" width="2" height="9"/><rect x="21" y="15" width="2" height="9"/><rect x="3" y="25" width="24" height="3"/></svg></div>
<div class="abs pico" style="left:723px;top:3103px"><svg width="30" height="30" viewBox="0 0 30 30" fill="none" stroke="var(--navy)" stroke-width="2.5"><circle cx="15" cy="15" r="12"/><path d="M6 24L24 6"/><circle cx="12" cy="13" r="4"/></svg></div>

<!-- numbers -->
<div class="abs pnum" style="left:479px;top:3171px">01</div>
<div class="abs pnum" style="left:446px;top:3297px">02</div>
<div class="abs pnum" style="left:486px;top:3379px">03</div>
<div class="abs pnum" style="left:587px;top:3406px">04</div>
<div class="abs pnum" style="left:686px;top:3384px">05</div>
<div class="abs pnum" style="left:728px;top:3297px">06</div>
<div class="abs pnum" style="left:693px;top:3171px">07</div>

<!-- principle texts -->
<div class="abs ptext right" style="left:130px;top:3105px;width:262px"><h4>Public Good Only</h4><p>Public Officials Should Only Serve The Public Good. Not Private Interests.</p></div>
<div class="abs ptext right" style="left:130px;top:3238px;width:218px"><h4>Truth Over Loyalty</h4><p>Major Government Decisions Should Be Based On Truth, And Rigorous Evidence. Not Party Loyalty, Pressure, Or Donors.</p></div>
<div class="abs ptext right" style="left:160px;top:3394px;width:242px"><h4>Clear Reasoning</h4><p>When A Public Decision Is Made, People Should Be Able To See The Reasoning. Clearly. Honestly. On The Record.</p></div>
<div class="abs ptext mid" style="left:468px;top:3518px;width:262px"><h4>Right To Challenge</h4><p>And If The Government Reasoning Is Flawed, Citizens Should Have A Way To Challenge It, And Get A Real Response.</p></div>
<div class="abs ptext" style="left:789px;top:3395px;width:270px"><h4>Disclose Conflicts</h4><p>Conflicts Of Interest In Public Office All Should Be Disclosed, Before Decisions Are Made.</p></div>
<div class="abs ptext" style="left:856px;top:3252px;width:196px"><h4>Real Consequences</h4><p>Lying Or Misleading The Public In Official Decisions Should Carry Consequences. Real Ones.</p></div>
<div class="abs ptext" style="left:807px;top:3109px;width:256px"><h4>People Before Money</h4><p>And Most Importantly, Money Should Never Outweigh People’s Voice.</p></div>

<!-- survey -->
<div class="abs center-head" style="top:3760px">
  <div class="eyebrow">THE SURVEY</div>
  <h2>The Survey <span class="serif">Real Results</span></h2>
</div>
<svg class="abs" style="left:452px;top:3826px" width="150" height="10" viewBox="0 0 150 10"><path d="M2 7Q75 1 148 6" fill="none" stroke="var(--red)" stroke-width="3" stroke-linecap="round"/></svg>
<div class="abs card">
  <div class="abs row" style="top:11px"><span class="k">National Pre-Registered Study (N=2,500 Representative)</span><span class="v">89.9%</span></div>
  <div class="abs row" style="top:77px"><span class="k">Agree With The 7 Principles</span><span class="v">89.9%</span></div>
  <div class="abs row" style="top:141px"><span class="k">Support Legal Framework Built Around Them</span><span class="v">82.9%</span></div>
  <div class="abs row" style="top:206px"><span class="k">Neutral</span><span class="v">14.4%</span></div>
  <div class="abs row last" style="top:268px"><span class="k">Actively Opposed</span><span class="v">2.7%</span></div>
  <div class="abs stress">
    STRESS TEST — Full Legal Framework, Enforcement Model, Actual Mechanism. Support HELD.<br>
    <b>Democrats: 84.5%</b> &nbsp;| &nbsp;&nbsp;<b>Republicans: 80.2%</b> &nbsp;| &nbsp;&nbsp;<b>Independents: 79.9%</b><br>
    They All Said YES.
  </div>
</div>

<!-- call to action -->
<section class="abs cta" role="img" aria-label="Soft red photograph of a flag and a crowd beneath the call to action">
  <h2 class="abs">We Deserve A Government<br>Legally Required <span class="serif">To Serve The<br>People Honestly.</span></h2>
  <p class="abs">Across Political Lines, Generations, And Races, Americans Are Arriving At The Same Conclusion. And We Don’t Have To Ask For It. We Just Have To Vote For It.</p>
  <div class="abs btn">VOTE YES
    <svg width="22" height="10" viewBox="0 0 22 10"><path d="M0 5h20M16 1l4 4-4 4" fill="none" stroke="var(--navy)" stroke-width="1.6"/></svg>
  </div>
  <div class="abs count">
    <svg width="56" height="50" viewBox="0 0 56 50" fill="none" stroke="var(--red)" stroke-width="3"><rect x="18" y="2" width="24" height="44" rx="4"/><rect x="6" y="14" width="20" height="18"/><path d="M11 23l4 4 7-7"/></svg>
    <div class="n">1016</div>
    <div class="l">People Already Voted<br>Yes For The Ballot</div>
  </div>
</section>

<!-- footer -->
<footer class="abs footer">
  <div class="abs brand"><span class="mark"></span><span class="name">Lantern Square</span></div>
  <div class="abs fsocial"><span class="on"></span><span></span><span></span><span></span></div>
  <div class="abs frule"></div>
  <div class="abs copy">© 2026 LANTERN SQUARE, STEADY COURSE. All Rights Reserved.</div>
</footer>

</body>
</html>
```